Lunaform website scandinavian interior design

Existing website: http://lunaform-example.no/

Webdesign for interior designer Ragna Tveitmo. The company name is Lunaform. Scandinavian interiør is known to be simple and elegant. The website will be in Norwegian, we are working on the text. The website needs to have a few more pages than just the front page. Here are the different titles of the pages:

1. Hjem
2. Om Lunaform
3. Tjenester og priser
4.. Kontakt oss

There should be Chatterloop and Pixelane icons somewhere at the bottom of the website.

The logo we want to use is attached (pink with black print, see attachment )

We have attached images for inspiration. We want to use some of these colors. The color in the logo, The style should be elegant, modern and delicate.

It is imprtant that the website is user friendly.

Target Market(s)

People who want to decorate their home
Companies and public sector who need to redecorate

Industry/Entity Type

Interior Designer

Coding

Coded - Design and coding required

Number of Pages Required

5+ page

Font styles to use
Other font styles liked:
• see example in the logo breakdown

Requirements
Must have
• Elegant, modern and delicate design
Images of design, see examples attached
Colors similar to the pictures
Should not have
• Too bright colors
Pictures of people

```html
<!DOCTYPE html>
<html lang="no">
<head>
<meta charset="utf-8">
<title>Lunaform – Interiørarkitekt Ragna Tveitmo</title>
<link href="https://fonts.googleapis.com/css2?family=Pinyon+Script&family=Cormorant+Garamond:wght@500;600&family=Montserrat:wght@400;600&family=Roboto+Condensed:wght@700&display=swap" rel="stylesheet">
<style>
:root{
  --blush:#f1ddd6;
  --blush-soft:#f7ecea;
  --ink:#151515;
  --text:#3a3a3a;
  --muted:#9a9a9a;
  --white:#ffffff;
  --line:#d9d2cf;
}
*{box-sizing:border-box;margin:0;padding:0}
html,body{width:1200px;height:4140px;overflow:hidden;background:var(--white)}
body{position:relative;font-family:'Montserrat',sans-serif;color:var(--text)}
.abs{position:absolute}
.photo{position:absolute}
.script{font-family:'Pinyon Script',cursive;color:var(--ink);font-weight:400}
.body-copy{font-size:15px;line-height:26px;text-align:center;color:var(--text)}
.link-cta{font-size:14px;font-weight:600;letter-spacing:1px;color:var(--ink);display:flex;align-items:center;gap:10px}
.btn-dark{background:var(--ink);color:var(--white);font-size:13px;font-weight:600;letter-spacing:1px;display:flex;align-items:center;justify-content:center;gap:10px}

/* header */
.site-header{left:0;top:0;width:1200px;height:100px;background:var(--blush)}
.social-mini{left:96px;top:40px;font-size:11px;color:var(--ink);display:flex;gap:12px}
.main-nav a{position:absolute;top:40px;font-family:'Cormorant Garamond',serif;font-weight:600;font-size:15px;color:var(--ink);text-decoration:none;white-space:nowrap}
.brand{left:540px;top:30px;width:120px;text-align:center;font-family:'Cormorant Garamond',serif;font-weight:600;font-size:28px;color:var(--ink)}
.search{left:1030px;top:40px;font-size:12px;color:var(--muted);display:flex;align-items:center;gap:14px}

/* hero */
.hero-living{left:23px;top:113px;width:572px;height:479px;background:linear-gradient(135deg,#e9e4dd,#b9a596 60%,#7a5c48)}
.hero-office{left:611px;top:113px;width:566px;height:479px;background:linear-gradient(160deg,#dcdcdc,#6d6d6d 55%,#3e3b39)}
.intro-title{left:0;top:660px;width:1200px;text-align:center;font-size:56px}
.intro-copy{left:160px;top:738px;width:880px}
.intro-cta{left:540px;top:806px}

/* about */
.about-band{left:0;top:960px;width:1200px;height:421px;background:var(--blush-soft)}
.about-room{left:365px;top:915px;width:401px;height:466px;background:linear-gradient(180deg,#c6a27c,#efe6dc 40%,#a68b70)}
.about-frame{left:162px;top:986px;width:381px;height:437px;background:var(--white);box-shadow:0 2px 10px rgba(0,0,0,.12)}
.about-portrait{left:185px;top:1009px;width:343px;height:388px;background:linear-gradient(160deg,#a3a5a8,#b66e66 55%,#5a4c46)}
.about-card{left:679px;top:1035px;width:372px;height:252px;background:var(--white);padding:28px 24px}
.about-card h2{font-size:40px;margin-bottom:8px}
.about-card p{font-size:10px;line-height:17px;color:var(--muted)}
.about-card .btn-dark{width:110px;height:34px;margin-top:16px;font-size:11px}

/* testimonials */
.quote-title{left:0;top:1480px;width:1200px;text-align:center;font-size:58px}
.quote-copy{left:240px;top:1580px;width:720px;font-size:14px;line-height:24px}
.arrow-left{left:192px;top:1608px}
.arrow-right{left:990px;top:1608px}
.quote-author{left:498px;top:1714px;display:flex;align-items:center;gap:14px}
.avatar{width:46px;height:46px;border-radius:50%;background:linear-gradient(135deg,#c99a86,#5a3d34)}
.author-name{font-family:'Roboto Condensed',sans-serif;font-size:17px;color:var(--ink);letter-spacing:.5px}
.author-handle{font-size:12px;color:var(--muted)}

/* services */
.services-band{left:0;top:2125px;width:1200px;height:220px;background:var(--blush-soft)}
.service-img{top:1853px;width:314px;height:411px}
.svc-private{left:100px;background:linear-gradient(180deg,#f2ece4,#d2ad86 50%,#c9c3bd)}
.svc-public{left:443px;background:linear-gradient(180deg,#ece9e4,#d9d4cc 45%,#4f4a45)}
.svc-supply{left:789px;background:linear-gradient(180deg,#f1f0ee,#e1ddd7 45%,#b48a5f)}
.service-label{top:2238px;width:230px;height:55px;background:var(--white);border:1px solid var(--line);display:flex;align-items:center;justify-content:center;font-family:'Cormorant Garamond',serif;font-weight:600;font-style:italic;font-size:17px;letter-spacing:1px;color:var(--ink)}

/* works */
.works-title{left:0;top:2405px;width:1200px;text-align:center;font-size:52px}
.work-back{background:var(--blush-soft)}
.work-img{background:linear-gradient(160deg,#eef0f1,#bfc4c7 60%,#8a8f92)}
.work-caption{text-align:center}
.work-caption h3{font-family:'Roboto Condensed',sans-serif;font-size:17px;color:var(--ink)}
.work-caption span{font-size:10px;color:var(--muted)}

/* call to action */
.cta-band{left:0;top:3454px;width:1200px;height:314px;background:var(--blush-soft)}
.cta-title{left:0;top:3500px;width:1200px;text-align:center;font-size:54px}
.cta-copy{left:220px;top:3583px;width:760px}
.cta-btn{left:518px;top:3655px;width:164px;height:48px}

/* gallery */
.gallery-band{left:0;top:3800px;width:1200px;height:258px;background:var(--blush-soft)}
.gallery-title{left:0;top:3830px;width:1200px;text-align:center;font-size:30px}
.gallery-img{top:3880px;width:154px;height:172px}

/* footer */
.footer-nav{left:100px;top:4090px;display:flex;gap:24px;font-family:'Cormorant Garamond',serif;font-weight:600;font-size:15px;color:var(--ink)}
.footer-social{left:560px;top:4092px;display:flex;gap:18px;font-size:12px;color:var(--ink)}
.copyright{right:100px;top:4092px;font-size:12px;color:var(--text)}
</style>
</head>
<body>

<header class="abs site-header">
  <div class="abs social-mini"><span>Chatterloop</span><span>Pixelane</span></div>
  <nav class="main-nav">
    <a style="left:307px">Hjem</a>
    <a style="left:410px">Om Lunaform</a>
    <a style="left:682px">Tjenester og priser</a>
    <a style="left:851px">Kontakt oss</a>
  </nav>
  <div class="abs brand">Lunaform</div>
  <div class="abs search">Search
    <svg width="18" height="18" viewBox="0 0 18 18"><circle cx="7.5" cy="7.5" r="5.5" fill="none" stroke="#151515" stroke-width="1.5"/><line x1="11.5" y1="11.5" x2="16" y2="16" stroke="#151515" stroke-width="1.5"/></svg>
  </div>
</header>

<div class="photo hero-living" role="img" aria-label="Lyst stueinteriør med skinnsofa og stort vindu"></div>
<div class="photo hero-office" role="img" aria-label="Kontorlandskap med murvegg og arbeidsbord"></div>

<h1 class="abs script intro-title">Interiørarkitekt Ragna Tveitmo</h1>
<p class="abs body-copy intro-copy">Sed ut perspiciatis unde omnis iste natus error sit voluptatem accusantium doloremque laudantium, totam rem aperiam, eaque ipsa quae ab illo inventore veritatis et quasi architecto beatae vitae dicta sunt explicabo.</p>
<div class="abs link-cta intro-cta">LET'S CHAT
  <svg width="26" height="12" viewBox="0 0 26 12"><path d="M0 6H24M19 1l5 5-5 5" fill="none" stroke="#151515" stroke-width="1.5"/></svg>
</div>

<section>
  <div class="abs about-band"></div>
  <div class="photo about-room" role="img" aria-label="Interiørdetalj med lampe, bilde og plante"></div>
  <div class="abs about-frame"></div>
  <div class="photo about-portrait" role="img" aria-label="Portrett av interiørarkitekten"></div>
  <div class="abs about-card">
    <h2 class="script">Om meg</h2>
    <p>Sed ut perspiciatis unde omnis iste natus error sit voluptatem accusantium doloremque laudantium, totam rem aperiam, eaque ipsa quae ab illo inventore veritatis et quasi architecto beatae vitae dicta sunt explicabo. Nemo enim ipsam voluptatem quia voluptas sit aspernatur.</p>
    <div class="btn-dark">LEARN MORE</div>
  </div>
</section>

<section>
  <h2 class="abs script quote-title">Hva De Sier?</h2>
  <svg class="abs arrow-left" width="16" height="28" viewBox="0 0 16 28"><path d="M14 2L3 14l11 12" fill="none" stroke="#3a3a3a" stroke-width="2"/></svg>
  <p class="abs body-copy quote-copy">Sed ut perspiciatis unde omnis iste natus error sit voluptatem accusantium doloremque laudantium, totam rem aperiam, eaque ipsa quae ab illo inventore veritatis et quasi architecto beatae vitae dicta sunt explicabo. Sed ut perspiciatis unde omnis iste natus error sit voluptatem accusantium doloremque laudantium, totam rem aperiam, eaque ipsa quae ab illo inventore</p>
  <svg class="abs arrow-right" width="16" height="28" viewBox="0 0 16 28"><path d="M2 2l11 12L2 26" fill="none" stroke="#3a3a3a" stroke-width="2"/></svg>
  <div class="abs quote-author">
    <div class="avatar" role="img" aria-label="Profilbilde av kunden"></div>
    <div><div class="author-name">INGRID SOLBERG</div><div class="author-handle">@sitat.no</div></div>
  </div>
</section>

<section>
  <div class="abs services-band"></div>
  <div class="photo service-img svc-private" role="img" aria-label="Privat stue med lys sofa og treverk"></div>
  <div class="photo service-img svc-public" role="img" aria-label="Spiserom med hvite stoler under skråtak"></div>
  <div class="photo service-img svc-supply" role="img" aria-label="Arbeidsplass med svart stol og skisser på veggen"></div>
  <div class="abs service-label" style="left:142px">PRIVATE INTERIØR</div>
  <div class="abs service-label" style="left:485px">CORPORATE / PUBLIC</div>
  <div class="abs service-label" style="left:831px">SUPPLIERS</div>
</section>

<section>
  <h2 class="abs script works-title">Se mine siste verk</h2>

  <div class="photo work-img" style="left:194px;top:2522px;width:366px;height:318px" role="img" aria-label="Lyst kontorlandskap med store vinduer"></div>
  <div class="abs work-caption" style="left:194px;top:2852px;width:366px"><h3>LATEST PROJECT TITLE ONE</h3><span>Interiør prosjekt</span></div>

  <div class="abs work-back" style="left:605px;top:2506px;width:404px;height:452px"></div>
  <div class="photo work-img" style="left:621px;top:2522px;width:372px;height:421px;background:linear-gradient(180deg,#f3f3f3,#e2ddd6 55%,#b99a78)" role="img" aria-label="Spisestue med trebord og bildevegg"></div>
  <div class="abs work-caption" style="left:621px;top:2966px;width:372px"><h3>LATEST PROJECT TITLE ONE</h3><span>Interiør prosjekt</span></div>

  <div class="abs work-back" style="left:194px;top:2937px;width:388px;height:400px"></div>
  <div class="photo work-img" style="left:210px;top:2953px;width:356px;height:368px;background:linear-gradient(180deg,#dcdad7,#c09466 50%,#3c3c3c)" role="img" aria-label="Soverom med seng og stripete teppe"></div>
  <div class="abs work-caption" style="left:210px;top:3344px;width:356px"><h3>LATEST PROJECT TITLE ONE</h3><span>Interiør prosjekt</span></div>

  <div class="photo work-img" style="left:621px;top:3034px;width:372px;height:287px;background:linear-gradient(180deg,#e8e8e8,#cfcfcf 50%,#4a4645)" role="img" aria-label="Stue med salongbord og grafisk kunst"></div>
  <div class="abs work-caption" style="left:621px;top:3344px;width:372px"><h3>LATEST PROJECT TITLE ONE</h3><span>Interiør prosjekt</span></div>
</section>

<section>
  <div class="abs cta-band"></div>
  <h2 class="abs script cta-title">Er du klar til å jobbe sammen?</h2>
  <p class="abs body-copy cta-copy">Sed ut perspiciatis unde omnis iste natus error sit voluptatem accusantium doloremque laudantium, totam rem aperiam, eaque ipsa quae ab illo inventore veritatis et quasi architecto</p>
  <div class="abs btn-dark cta-btn">LET'S CHAT
    <svg width="22" height="12" viewBox="0 0 22 12"><path d="M0 6H20M15 1l5 5-5 5" fill="none" stroke="#fff" stroke-width="1.5"/></svg>
  </div>
</section>

<section>
  <div class="abs gallery-band"></div>
  <h2 class="abs script gallery-title">Følg med på stilene våre på Pixelane</h2>
  <div class="photo gallery-img" style="left:100px;background:linear-gradient(180deg,#f2f2f0,#cfc6bb)" role="img" aria-label="Lyst rom med planter"></div>
  <div class="photo gallery-img" style="left:269px;background:linear-gradient(180deg,#eeeeec,#d7b08a)" role="img" aria-label="Hylle med klokke og dekor"></div>
  <div class="photo gallery-img" style="left:438px;background:linear-gradient(180deg,#f0efec,#b9b2a8)" role="img" aria-label="Kjøkken med trebord"></div>
  <div class="photo gallery-img" style="left:607px;background:linear-gradient(180deg,#fafafa,#e6e3de)" role="img" aria-label="Hvitt soverom"></div>
  <div class="photo gallery-img" style="left:776px;background:linear-gradient(180deg,#d7dadd,#3f4f63)" role="img" aria-label="Kjøkken med blå skap"></div>
  <div class="photo gallery-img" style="left:945px;width:155px;background:linear-gradient(180deg,#5f7a52,#c9b28e)" role="img" aria-label="Arbeidsrom med grønn vegg"></div>
</section>

<footer>
  <nav class="abs footer-nav"><span>Hjem</span><span>Om Lunaform</span><span>Tjenester og priser</span><span>Kontakt oss</span></nav>
  <div class="abs footer-social"><span>Chatterloop</span><span>Pixelane</span></div>
  <div class="abs copyright">© 2020 Lunaform. All Rights Reserved</div>
</footer>

</body>
</html>
```